Construction machinery rental / heavy equipment rental needs a nice billboard

We need a billboard for our company.
We rent out construction machinery such as excavators, wheel loaders, wheel dumpers and so on...

I would like an elegant, simple, dark design.
Colors: black yellow grey white

The following must be on the billboard:
Logo
phone number: 078 / 513 90 41
website: www.kiesgrube-talwerk.ch
the machines I rent out: Bagger bis 10T, Radlader, Dumper, Raupenkipper

the font in the logo is: Square 721

Final format 2950 x 1900mm
I have uploaded pictures:
"Excavator 1-6" are my pictures, which can be used
"Sample 1-4" are pictures whose style I like
"Billboard" are billboards which I like

Requirements
Must have
• The following must be on the billboard: Logo phone number: 078 / 513 90 41 website: www.kiesgrube-talwerk.ch the machines I rent out: Bagger bis 10T, Radlader, Dumper, Raupenkipper

```html
<!DOCTYPE html>
<html lang="de">
<head>
<meta charset="utf-8">
<title>Talwerk Baumaschinen – Billboard</title>
<link href="https://fonts.googleapis.com/css2?family=Krona+One&display=swap" rel="stylesheet">
<style>
  :root {
    --stage: #6c6f72;
    --board: #000000;
    --white: #ffffff;
    --gold: #d4b93c;
    --gold-light: #efe08a;
    --gold-dark: #9c8420;
    --machine-light: #4a5060;
    --machine-mid: #2a2e38;
    --machine-dark: #14161c;
    --machine-accent: #c4542a;
  }
  * { margin: 0; padding: 0; box-sizing: border-box; }
  html, body {
    width: 694px; height: 1200px; overflow: hidden;
    background: var(--stage);
  }
  .billboard {
    position: absolute;
    left: 37px; top: 400px;
    width: 620px; height: 399px;
    background: var(--board);
    box-shadow: 6px 8px 14px rgba(0,0,0,.45);
    overflow: hidden;
    font-family: "Krona One", sans-serif;
    color: var(--white);
  }
  .machine-photo {
    position: absolute;
    left: 242px; top: 0;
    width: 372px; height: 340px;
    border-radius: 0 0 18px 18px;
    background:
      radial-gradient(ellipse 18% 10% at 68% 66%, rgba(196,84,42,.55) 0%, rgba(196,84,42,0) 100%),
      radial-gradient(ellipse 60% 55% at 40% 55%, var(--machine-light) 0%, var(--machine-mid) 45%, var(--machine-dark) 80%),
      var(--machine-dark);
  }
  .brand {
    position: absolute;
    left: 29px; top: 30px;
    display: flex; align-items: center; gap: 9px;
  }
  .brand-mark {
    width: 22px; height: 22px;
    background: var(--gold);
  }
  .brand-name {
    font-size: 27px;
    color: var(--gold);
    letter-spacing: .5px;
  }
  .headline {
    position: absolute;
    left: 27px; top: 136px;
    font-size: 31px;
    letter-spacing: -1px;
    line-height: 1;
  }
  .headline .accent {
    background: linear-gradient(90deg, var(--gold-dark), var(--gold-light) 50%, var(--gold));
    -webkit-background-clip: text; background-clip: text;
    color: transparent;
  }
  .fleet {
    position: absolute;
    left: 27px; top: 182px;
    width: 198px;
    list-style: none;
    border-top: 1px solid var(--gold);
  }
  .fleet li {
    height: 29.5px;
    display: flex; align-items: center;
    font-size: 16px;
    letter-spacing: -.6px;
    white-space: nowrap;
    border-bottom: 1px solid var(--gold);
  }
  .phone {
    position: absolute;
    left: 27px; top: 346px;
    width: 213px; height: 24px;
    display: flex;
    border: 1px solid var(--gold);
  }
  .phone-icon {
    width: 26px; height: 100%;
    display: flex; align-items: center; justify-content: center;
  }
  .phone-number {
    flex: 1;
    background: linear-gradient(90deg, var(--gold) 0%, var(--gold-light) 55%, var(--gold) 100%);
    color: var(--board);
    font-size: 16px;
    letter-spacing: -.8px;
    white-space: nowrap;
    display: flex; align-items: center;
    padding-left: 5px;
  }
  .website {
    position: absolute;
    right: 26px; top: 352px;
    font-size: 12.5px;
    letter-spacing: -.5px;
    white-space: nowrap;
  }
</style>
</head>
<body>
  <section class="billboard">
    <div class="machine-photo" role="img" aria-label="Foto eines schwarzen Minibaggers mit grosser Schaufel im Vordergrund"></div>

    <div class="brand">
      <span class="brand-mark"></span>
      <span class="brand-name">TALWERK</span>
    </div>

    <h1 class="headline">WE <span class="accent">RENT</span></h1>

    <ul class="fleet">
      <li>BAGGER BIS 10T</li>
      <li>RADLADER</li>
      <li>DUMPER</li>
      <li>RAUPENKIPPER</li>
    </ul>

    <div class="phone">
      <span class="phone-icon">
        <svg width="14" height="14" viewBox="0 0 24 24" aria-hidden="true">
          <path fill="#d4b93c" d="M6.6 10.8c1.4 2.8 3.8 5.1 6.6 6.6l2.2-2.2c.3-.3.7-.4 1-.2 1.1.4 2.3.6 3.6.6.6 0 1 .4 1 1V20c0 .6-.4 1-1 1C10.6 21 3 13.4 3 4c0-.6.4-1 1-1h3.5c.6 0 1 .4 1 1 0 1.3.2 2.5.6 3.6.1.3 0 .7-.2 1l-2.3 2.2z"/>
        </svg>
      </span>
      <span class="phone-number">078 / 513 90 41</span>
    </div>

    <p class="website">www.kiesgrube-talwerk.ch</p>
  </section>
</body>
</html>
```